Martin Hale PA Card Logo

Current logo attached. Its 25 year old logo I have used. Looking for a new fresh elegant professional look/design for a law firm that has high net worth clientele and is estate planning business law firm. Firm mis in Palm Beach Florida.
One sided card linen stock white will be used. Logo section name section. Logo should include nice elegant design using the letter "M" perhapa (I am not wed to current font of the M on current logo.) Be creative there with logo design. My initials are MH.......color scheme I figure 3 tone... Raised Gold Foil, Blue name of firm = Martin Hale, P.A. My practice focus is Family and Business Asset Protection. My name is Martin M. Hale, Esq. Practice specialties include Asset Protection trusts, Business Succession Planning, LLC law, Estate Planning, Medicaid Planning (Maybe put those topics in bullets in a section of card. Bottom of card can be reserved smaller print address phone website and email address. Address section is not as important as logo and topics of practice on front. I foresee address section can be in dark blue. MY name and Topics dark blue as well.
Target Market(s)
affluent; business owners executives; wealth 2-10 million net worth
Industry/Entity Type
business law and estate planning
Contact Information for Business Card
White thick linen one sided

```html
<!DOCTYPE html>
<html lang="en">
<head>
<meta charset="UTF-8">
<title>Martin Hale, P.A. — Business Card</title>
<link rel="stylesheet" href="https://fonts.googleapis.com/css2?family=Cormorant+Garamond:wght@500;600;700&display=swap">
<style>
  :root {
    --page: #ffffff;
    --card: #e9e7e5;
    --navy: #1c3650;
    --gold: #bf9b17;
  }
  * { margin: 0; padding: 0; box-sizing: border-box; }
  html, body {
    width: 1200px;
    height: 1200px;
    overflow: hidden;
    background: var(--page);
  }
  .card {
    position: absolute;
    left: 365px;
    top: 246px;
    width: 477px;
    height: 715px;
    background: var(--card);
    color: var(--navy);
    font-family: "Cormorant Garamond", Georgia, serif;
    font-variant-numeric: lining-nums;
    text-align: center;
  }
  .card > * {
    position: absolute;
    left: 0;
    width: 100%;
  }
  .monogram {
    top: 50px;
    height: 154px;
    font-size: 140px;
    font-weight: 600;
    line-height: 154px;
    color: var(--gold);
    letter-spacing: 2px;
  }
  .firm-name {
    top: 234px;
    font-size: 38px;
    font-weight: 600;
    letter-spacing: 0.5px;
    line-height: 1;
  }
  .tagline {
    top: 284px;
    font-size: 13.5px;
    font-weight: 600;
    letter-spacing: 2.8px;
    line-height: 1;
  }
  .practice-areas {
    top: 328px;
    list-style: none;
  }
  .practice-areas li {
    font-size: 26.5px;
    font-weight: 600;
    line-height: 34.5px;
  }
  .practice-areas li::before {
    content: "• ";
    font-size: 20px;
    vertical-align: 3px;
  }
  .contact {
    top: 532px;
    font-style: normal;
  }
  .contact span {
    display: block;
    font-size: 26.5px;
    font-weight: 600;
    line-height: 33px;
  }
  .contact .location { margin-top: 5px; }
</style>
</head>
<body>
  <section class="card">
    <div class="monogram">MH</div>
    <h1 class="firm-name">MARTIN HALE, P.A.</h1>
    <p class="tagline">FAMILY &amp; BUSINESS ASSET PROTECTION</p>
    <ul class="practice-areas">
      <li>Asset Protection Trusts</li>
      <li>Business Succession Planning</li>
      <li>LLC Law</li>
      <li>Estate Planning</li>
      <li>Medicaid Planning</li>
    </ul>
    <address class="contact">
      <span class="phone">(555) 214-3380</span>
      <span class="email">info@martinhalepa.com</span>
      <span class="website">www.martinhalepa.com</span>
      <span class="location">Harbor Point, Florida</span>
    </address>
  </section>
</body>
</html>
```